Varneck Law Business cards and stationary design project

We are looking for a stationary design for business cards (double sided), 8x10, 5x7, and legal and standard envelopes.

We would like the design to match the logo that we have already.
Color palate preferred is Teal, White, grey and any others that will look good for a professional law firm.

We would like this statement: "RELATIONSHIPS. RESPECT. RESULT" to be on the back of the business cards and maybe on the stationary if it looks good.

Please see link to website for more information: www.varneck-law-example.com

Target Market(s)

Potential clients that need Attorney services.

Industry/Entity Type

Law Firm

Contact Information for Business Card

We would like the front and back to be two different colors. Current business cards are teal front, grey back and are a vertical design. We are open to options with colors.

Font styles to use
Serif

Colors
33a6d7
33b8a4
b9b9b9
5c5c5c

Requirements
Must have
• Logo supplied needs to go on the card and stationary.
• Match website color palate, www.varneck-law-example.com
• Be professional and not too wordy.
• Criminal Law, Civil Litigation, Personal Injury, Restraining Orders need to be on the card.
Nice to have
• RELATIONSHIPS. RESPECT. RESULTS. on the back of the card.
Should not have
• Not be too busy/wordy or too flashy.

```html
<!DOCTYPE html>
<html lang="en">
<head>
<meta charset="utf-8">
<title>Varneck Law — Business Card</title>
<link rel="stylesheet" href="https://fonts.googleapis.com/css2?family=Cinzel:wght@400;500&display=swap">
<style>
  :root {
    --page-bg: #e6eaea;
    --card-white: #ffffff;
    --brand-teal: #1fa39c;
    --back-teal: #29a8a4;
    --band-gold: #d5c964;
    --rule-gold: #d8c85a;
    --band-text: #3b3a2c;
    --url-gold: #ddd27a;
    --text-white: #ffffff;
  }
  * { margin: 0; padding: 0; box-sizing: border-box; }
  html, body {
    width: 1200px;
    height: 900px;
    overflow: hidden;
    background: var(--page-bg);
    font-family: "Cinzel", Georgia, serif;
  }
  .sheet {
    position: relative;
    width: 1200px;
    height: 900px;
    display: flex;
    align-items: center;
    justify-content: center;
    gap: 44px;
  }
  .card {
    position: relative;
    width: 520px;
    height: 312px;
    overflow: hidden;
    box-shadow: 0 3px 10px rgba(0, 0, 0, 0.18);
  }

  /* Front */
  .card-front { background: var(--card-white); }
  .brand {
    position: absolute;
    left: 0;
    top: 50px;
    width: 250px;
    display: flex;
    flex-direction: column;
    align-items: center;
  }
  .brand-mark {
    width: 64px;
    height: 64px;
    border-radius: 50%;
    background: var(--brand-teal);
  }
  .firm-name {
    margin-top: 22px;
    white-space: nowrap;
    font-size: 25px;
    line-height: 30px;
    font-weight: 400;
    color: var(--brand-teal);
    letter-spacing: 0.5px;
  }
  .contact {
    position: absolute;
    left: 273px;
    top: 62px;
    height: 122px;
    padding-left: 10px;
    border-left: 2px solid var(--rule-gold);
    color: var(--brand-teal);
    font-size: 13px;
    line-height: 19px;
    white-space: nowrap;
  }
  .contact .address { margin-bottom: 12px; }
  .gold-rule {
    position: absolute;
    left: 0;
    top: 231px;
    width: 100%;
    height: 3px;
    background: var(--rule-gold);
  }
  .practice-band {
    position: absolute;
    left: 0;
    top: 240px;
    width: 100%;
    height: 72px;
    background: var(--band-gold);
    text-align: center;
  }
  .practice-title {
    margin-top: 12px;
    font-size: 14px;
    letter-spacing: 4px;
    color: var(--text-white);
  }
  .practice-list {
    margin-top: 12px;
    font-size: 12px;
    color: var(--band-text);
    letter-spacing: 0.3px;
  }
  .practice-list .divider { margin: 0 6px; }

  /* Back */
  .card-back { background: var(--back-teal); }
  .motto {
    position: absolute;
    left: 38px;
    top: 36px;
    font-size: 36px;
    line-height: 31px;
    color: var(--text-white);
    letter-spacing: 1px;
  }
  .website {
    position: absolute;
    right: 36px;
    bottom: 36px;
    font-size: 12px;
    letter-spacing: 2px;
    color: var(--url-gold);
  }
</style>
</head>
<body>
  <main class="sheet">
    <section class="card card-front" aria-label="Business card front">
      <div class="brand">
        <div class="brand-mark"></div>
        <div class="firm-name">Varneck Law</div>
      </div>
      <div class="contact">
        <p class="address">Southern California,<br>4470 Harbor View Rd. #210<br>Seacliff Bay, CA 90000</p>
        <p class="phone">(555) 014-2280</p>
        <p class="email">ava@varneck-law.com</p>
      </div>
      <div class="gold-rule"></div>
      <div class="practice-band">
        <p class="practice-title">PRACTICE AREAS:</p>
        <p class="practice-list">Criminal Law<span class="divider">|</span>Civil Litigation/Personal Injury<span class="divider">|</span>Restraining Orders</p>
      </div>
    </section>

    <section class="card card-back" aria-label="Business card back">
      <p class="motto">RELATIONSHIPS<br>RESPECT<br>RESULT</p>
      <p class="website">WWW.VARNECK-LAW-EXAMPLE.COM</p>
    </section>
  </main>
</body>
</html>
```